Red Sea Boat trips in need of Business Card for Private Boat Tours

We need a Business card for a new business set-up in Egypt on the Red Sea for private snorkelling and boat excursions to one of the world's most beautiful reefs. We have wording logo already set-up which matches the boat but we need business cards to be bright and colourful with pictures of boat

Industry/Entity Type

Tourism

Contact Information for Business Card

Two Silver Herons (font provided) Boat Trips

```html
<!DOCTYPE html>
<html lang="en">
<head>
<meta charset="utf-8">
<title>Two Silver Herons – Business Card</title>
<link href="https://fonts.googleapis.com/css2?family=Arimo:wght@400;700&display=swap" rel="stylesheet">
<style>
  :root {
    --page: #e6e6e6;
    --card: #ffffff;
    --ink: #111111;
    --muted: #555555;
    --rule: #c8c8c8;
    --sea-light: #2a9fb8;
    --sea-deep: #125a78;
    --hull: #e4e7ea;
    --seat: #b9c1cc;
  }
  html, body {
    margin: 0;
    width: 1200px;
    height: 1200px;
    overflow: hidden;
    background: var(--page);
    font-family: "Arimo", Arial, sans-serif;
  }
  .canvas { position: relative; width: 1200px; height: 1200px; }
  .card {
    position: absolute;
    width: 689px;
    height: 393px;
    box-sizing: border-box;
    background: var(--card);
    box-shadow: 0 6px 10px rgba(0,0,0,0.18);
  }
  .card--front { left: 267px; top: 159px; }
  .card--back  { left: 262px; top: 653px; overflow: hidden; }

  .brand {
    position: absolute;
    right: 49px;
    top: 68px;
    margin: 0;
    font-size: 37px;
    font-weight: 700;
    line-height: 44px;
    color: var(--ink);
    white-space: nowrap;
  }
  .person { position: absolute; left: 48px; top: 222px; }
  .person__name { margin: 0; font-size: 25px; line-height: 30px; font-weight: 700; color: var(--ink); }
  .person__role { margin: 2px 0 0; font-size: 13px; line-height: 16px; font-weight: 700; color: var(--muted); }
  .divider {
    position: absolute; left: 48px; right: 48px; top: 281px;
    height: 1px; background: var(--rule);
  }
  .contacts {
    position: absolute; left: 46px; top: 290px;
    list-style: none; margin: 0; padding: 0;
    font-size: 15.5px; color: var(--muted); line-height: 20.5px;
  }
  .contacts li { display: flex; align-items: center; gap: 8px; }
  .contacts svg { width: 14px; height: 14px; fill: var(--ink); flex: none; }
  .address {
    position: absolute; right: 44px; top: 292px;
    margin: 0; text-align: right; font-style: normal;
    font-size: 15.5px; color: var(--muted); line-height: 20.5px;
  }
  .boat-photo {
    width: 100%; height: 100%;
    background: linear-gradient(100deg,
      var(--sea-light) 0%,
      var(--sea-deep) 22%,
      var(--hull) 48%,
      var(--seat) 75%,
      var(--hull) 100%);
  }
</style>
</head>
<body>
<main class="canvas">
  <section class="card card--front">
    <h1 class="brand">Two Silver Herons</h1>
    <div class="person">
      <p class="person__name">Omar Haddad</p>
      <p class="person__role">President</p>
    </div>
    <div class="divider"></div>
    <ul class="contacts">
      <li>
        <svg viewBox="0 0 24 24"><path d="M6.6 10.8a15.1 15.1 0 0 0 6.6 6.6l2.2-2.2a1 1 0 0 1 1-.25 11.4 11.4 0 0 0 3.6.57 1 1 0 0 1 1 1V20a1 1 0 0 1-1 1A17 17 0 0 1 3 4a1 1 0 0 1 1-1h3.5a1 1 0 0 1 1 1c0 1.25.2 2.45.57 3.57a1 1 0 0 1-.25 1z"/></svg>
        555-210-4831
      </li>
      <li>
        <svg viewBox="0 0 24 24"><path d="M7 1h10a2 2 0 0 1 2 2v18a2 2 0 0 1-2 2H7a2 2 0 0 1-2-2V3a2 2 0 0 1 2-2zm0 3v14h10V4zm5 15.5a1.2 1.2 0 1 0 0 2.4 1.2 1.2 0 0 0 0-2.4z"/></svg>
        555-317-6092
      </li>
      <li>
        <svg viewBox="0 0 24 24"><path d="M2 5h20v14H2zm2 2v.5l8 5 8-5V7zm0 2.8V17h16V9.8l-8 5z"/></svg>
        info@twosilverherons.com
      </li>
    </ul>
    <address class="address">
      2140 Coral Reef Road<br>
      Hurghada, Egypt 84511<br>
      www.twosilverherons.com
    </address>
  </section>

  <section class="card card--back">
    <div class="boat-photo" role="img" aria-label="Photograph of a white cabin cruiser with navy bimini top and grey seating, moored in turquoise Red Sea water"></div>
  </section>
</main>
</body>
</html>
```